starlitmanesandtails pet therapy animals

I would like a business card to genarate posative emotions within people. My program has been running in a retirement village for over 5 years I work with residents and family members. My dogs work in palative care and are a great support to family members at the end stage. I also support the families and friends at furnerals when needed to dogs are always with me. Starlitmanes started with the death of my first therapy dog Oscar there was such an out cry of grief within the town and retirement village that he had his own furneral The hooves came into it when I was donated a beautiful Miniature horse for the pet therapy program with great results. I now need something very special as a business card. Eg Angelwings my dogs are King Charles Cavaliers so with what I have described can you create something beautiful to acknowledge to work I do and promote it more.
Updates

Project Deadline Extended
Reason: The reason I have extended the deadline to give other designers a chance to look at the job. So far I have 3 designs. I am hoping to get a few more.

Industry/Entity Type

Town

Contact Information for Business Card

Starlitmanesandtails pet therapy animals
Rosalind Tweedy
E-mail starlitmanesandtails@quillnet.example
Mobile 0461287039
Pet therapy animals give unconditional love to the aged and disabled.

Font styles to use
Decorative

Colors

Designer to choose colors to be used in the design.

Requirements
Nice to have
• angelwings a King Charles Cavalier tan and white with angel wings and a horse with angel wings

```html
<!DOCTYPE html>
<html lang="en">
<head>
<meta charset="utf-8">
<title>Starlitmanesandtails – Business Card</title>
<link rel="stylesheet" href="https://fonts.googleapis.com/css2?family=Cinzel:wght@600&family=Arimo:wght@400;700&display=swap">
<style>
  :root {
    --backdrop: #ece7e2;
    --front-centre: #ffffff;
    --front-edge: #f6bfd2;
    --back-fill: #b3245e;
    --brand-ink: #b02a63;
    --tagline-ink: #6f6a6c;
    --name-ink: #ffffff;
    --motto-ink: #f4c9da;
    --rule-ink: #d77fa3;
    --contact-ink: #ffffff;
    --icon-fill: #f6bfd2;
  }
  * { box-sizing: border-box; margin: 0; padding: 0; }
  html, body { width: 1200px; height: 581px; overflow: hidden; }
  body { background: var(--backdrop); position: relative; font-family: "Arimo", Arial, sans-serif; }

  .card-side { position: absolute; top: 145px; width: 473px; height: 291px; }
  .card-front {
    left: 127px;
    background: radial-gradient(ellipse 60% 75% at 52% 45%, var(--front-centre) 0%, var(--front-edge) 100%);
  }
  .card-back { left: 600px; background: var(--back-fill); }

  .brand { position: absolute; left: 90px; top: 108px; width: 300px; }
  .brand-row { display: flex; align-items: center; gap: 10px; }
  .brand-dot { width: 14px; height: 14px; border-radius: 50%; background: var(--brand-ink); flex: none; }
  .brand-name {
    font-family: "Cinzel", Georgia, serif; font-weight: 600; color: var(--brand-ink);
    font-size: 30px; line-height: 1.1;
  }
  .brand-name .line2 { display: block; padding-left: 24px; font-size: 26px; }
  .brand-tagline {
    margin-top: 10px; padding-left: 160px; font-weight: 700; font-size: 9px;
    color: var(--tagline-ink); letter-spacing: 0.2px; white-space: nowrap;
  }

  .holder-name {
    position: absolute; top: 130px; width: 100%; text-align: center;
    font-family: "Cinzel", Georgia, serif; font-weight: 600; font-size: 24px;
    color: var(--name-ink); letter-spacing: 0.5px;
  }
  .motto {
    position: absolute; left: 110px; top: 194px; width: 252px;
    border-top: 1px solid var(--rule-ink); border-bottom: 1px solid var(--rule-ink);
    padding: 3px 0 4px; text-align: center; font-size: 12.5px; line-height: 14px; color: var(--motto-ink);
  }
  .contacts {
    position: absolute; top: 235px; left: 52px; right: 0;
    display: flex; align-items: center; gap: 6px; white-space: nowrap;
    font-size: 13px; font-weight: 700; color: var(--contact-ink);
  }
  .contacts svg { flex: none; }
  .contacts .phone-icon { margin-left: 8px; }
</style>
</head>
<body>
  <section class="card-side card-front" aria-label="Card front">
    <div class="brand">
      <div class="brand-row">
        <span class="brand-dot"></span>
        <span class="brand-name">Starlitmanes<span class="line2">and tails</span></span>
      </div>
      <p class="brand-tagline">PET THERAPY ANIMALS</p>
    </div>
  </section>

  <section class="card-side card-back" aria-label="Card back">
    <h1 class="holder-name">Rosalind Tweedy</h1>
    <p class="motto">Pet therapy animals give unconditional love<br>to the aged and disabled.</p>
    <p class="contacts">
      <svg class="mail-icon" width="14" height="12" viewBox="0 0 14 12" aria-hidden="true">
        <rect x="0" y="0" width="14" height="12" rx="3" fill="var(--icon-fill)"/>
        <path d="M3 4 L7 7 L11 4" fill="none" stroke="var(--back-fill)" stroke-width="1.3"/>
      </svg>
      <span>starlitmanesandtails@quillnet.example</span>
      <svg class="phone-icon" width="12" height="13" viewBox="0 0 12 13" aria-hidden="true">
        <rect x="0" y="0" width="12" height="13" rx="2" fill="var(--icon-fill)"/>
        <path d="M4 2.5 C2 4.5 2 8.5 4 10.5 L5.5 9 L4.8 7.8 C4.2 7 4.2 6 4.8 5.2 L5.5 4 Z" fill="var(--back-fill)"/>
      </svg>
      <span>0461287039</span>
    </p>
  </section>
</body>
</html>
```